Indy Film Production Company/Studio

We need a business card designed from an existing logo. We are a digital studio/production company that caters to creating genre entertainment, like Action, Horror, and martial arts. The card along with the logo will be used to Brand the company from letter heads to banners. The design will also be used for postcards and Brochures. It should be professional and masculine.
Updates

Thank you to all the designers who have participated. I'm narrowing down who it will be. Thank you again.

Target Market(s)

Investors, Networks, Producers, and actors

Industry/Entity Type

Film Production

Contact Information for Business Card

Benedict Harlowe
Producer/Writer/Director
www.pelvarmotionworks.com

Requirements
Must have
• Website address, Facebook icon and Twitter icon possibly in the back of the card.
Nice to have
• Logline of Company: Follow The Action.

```html
<!DOCTYPE html>
<html lang="en">
<head>
<meta charset="utf-8">
<title>Pelvar Motion Works – Business Card</title>
<link href="https://fonts.googleapis.com/css2?family=Arimo:wght@400;700&display=swap" rel="stylesheet">
<style>
  :root {
    --backdrop: #26272b;
    --card: #1f1f20;
    --red: #e3141b;
    --red-line: #9c1217;
    --white: #f2f2f2;
    --text: #e6e6e6;
  }
  html, body {
    margin: 0;
    width: 1200px;
    height: 900px;
    overflow: hidden;
    background: var(--backdrop);
    font-family: "Arimo", Arial, sans-serif;
  }
  .canvas {
    position: relative;
    width: 1200px;
    height: 900px;
  }
  .card {
    position: absolute;
    width: 540px;
    height: 309px;
    background: var(--card);
    border-bottom: 6px solid var(--red);
    box-sizing: border-box;
  }
  .card--back { left: 90px; top: 110px; }
  .card--front { left: 570px; top: 480px; }

  /* wordmark */
  .wordmark {
    display: flex;
    align-items: center;
    gap: 10px;
    color: var(--red);
    font-weight: 700;
    text-transform: uppercase;
    line-height: 1;
  }
  .wordmark__square {
    width: 14px;
    height: 14px;
    background: var(--red);
    flex: none;
  }
  .wordmark__name { letter-spacing: 1px; }

  /* back side */
  .contact-list {
    position: absolute;
    left: 34px;
    top: 96px;
    margin: 0;
    padding: 0;
    list-style: none;
    color: var(--text);
    font-size: 13.5px;
  }
  .contact-list li {
    display: flex;
    align-items: center;
    gap: 12px;
    height: 22px;
  }
  .contact-list svg { width: 13px; height: 13px; flex: none; }
  .divider-vertical {
    position: absolute;
    left: 300px;
    top: 54px;
    width: 1px;
    height: 96px;
    background: var(--red-line);
  }
  .card--back .wordmark {
    position: absolute;
    left: 322px;
    top: 84px;
    font-size: 17px;
  }
  .divider-horizontal {
    position: absolute;
    left: 300px;
    top: 172px;
    width: 210px;
    height: 1px;
    background: var(--red-line);
  }
  .address {
    position: absolute;
    left: 304px;
    top: 186px;
    display: flex;
    gap: 8px;
    color: var(--text);
    font-size: 12px;
    line-height: 1.4;
  }
  .address svg { width: 11px; height: 14px; margin-top: 1px; flex: none; }

  /* front side */
  .card--front .wordmark {
    position: absolute;
    left: 0;
    right: 0;
    top: 138px;
    justify-content: center;
    font-size: 24px;
  }
  .card--front .wordmark__square { width: 18px; height: 18px; }
</style>
</head>
<body>
<main class="canvas">

  <section class="card card--back" aria-label="Card back with contact details">
    <ul class="contact-list">
      <li>
        <svg viewBox="0 0 16 16" aria-hidden="true"><path fill="#e3141b" d="M4 1l3 3-2 2c1 2 3 4 5 5l2-2 3 3-2 3C7 15 1 9 1 4z"/></svg>
        (555)-210-4476
      </li>
      <li>
        <svg viewBox="0 0 16 16" aria-hidden="true"><rect x="1" y="3" width="14" height="10" fill="#e3141b"/><path d="M1 3l7 6 7-6" stroke="#1f1f20" stroke-width="1.5" fill="none"/></svg>
        bharlowe@pelvarmotionworks.com
      </li>
      <li>
        <svg viewBox="0 0 16 16" aria-hidden="true"><circle cx="8" cy="8" r="6" fill="#e3141b"/></svg>
        /pelvarmotionworks
      </li>
      <li>
        <svg viewBox="0 0 16 16" aria-hidden="true"><circle cx="8" cy="8" r="6.5" fill="none" stroke="#e3141b" stroke-width="1.5"/><ellipse cx="8" cy="8" rx="3" ry="6.5" fill="none" stroke="#e3141b" stroke-width="1.2"/><path d="M1.5 8h13" stroke="#e3141b" stroke-width="1.2"/></svg>
        www.pelvarmotionworks.com
      </li>
      <li>
        <svg viewBox="0 0 16 16" aria-hidden="true"><circle cx="8" cy="8" r="6" fill="#e3141b"/></svg>
        @pelvarmotion
      </li>
    </ul>

    <div class="divider-vertical"></div>

    <div class="wordmark">
      <span class="wordmark__square"></span>
      <span class="wordmark__name">Pelvar Motion Works</span>
    </div>

    <div class="divider-horizontal"></div>

    <div class="address">
      <svg viewBox="0 0 12 16" aria-hidden="true"><path fill="#e3141b" d="M6 0a6 6 0 0 1 6 6c0 4-6 10-6 10S0 10 0 6a6 6 0 0 1 6-6z"/><circle cx="6" cy="6" r="2.2" fill="#1f1f20"/></svg>
      <span>14 Mill Lane<br>Harrow Falls New York 12490</span>
    </div>
  </section>

  <section class="card card--front" aria-label="Card front with company name">
    <div class="wordmark">
      <span class="wordmark__square"></span>
      <span class="wordmark__name">Pelvar Motion Works</span>
    </div>
  </section>

</main>
</body>
</html>
```